Power Point Template

I would like to have a power point template for our company.
See our website: www.brevikhamna.se for logo/colors and inspiration.

The template will be used for bank meetings etc, so it should be formal and professional.

Should show examples of various layouts.
Updates

I want the following headings/sections/example slides: - Slide with table of contents - Slide with bullets (just to show how a bullet list looks like) - Slide with project timeline - Slide with business case calculations (table e.g.) - slide with pictures with room for descriptive text (to show inspirational pictures, one slide per section: exterior, interior upper floor, exterior lower floor)? - Slide where our buildings are described (bullet list) - Slide with presentation of our business partners - First page with a faded background picture of our building (the one where our logo is shown)

Industry/Entity Type

It Company

```html
<!DOCTYPE html>
<html lang="en">
<head>
<meta charset="utf-8">
<title>Brevik Hamna – Presentation Template</title>
<link href="https://fonts.googleapis.com/css2?family=Montserrat:wght@400;600;700&family=Open+Sans:wght@400;600&display=swap" rel="stylesheet">
<style>
:root{
  --navy:#1e2b48;
  --gold:#f7b12e;
  --grey:#8e9196;
  --grey-light:#d4d5d7;
  --ink:#2b2f36;
  --muted:#7b7f86;
  --board:#dcdcdc;
  --white:#ffffff;
}
*{box-sizing:border-box;margin:0;padding:0}
html,body{width:1200px;height:1200px;overflow:hidden;background:var(--board)}
.board{
  width:1200px;height:1200px;
  display:grid;
  grid-template-columns:271px 301px 292px 246px;
  grid-auto-rows:141px;
  row-gap:20px;
  padding:18px 0 0 46px;
}
.slide{position:relative;width:246px;height:141px;background:var(--white);overflow:hidden;font-family:"Open Sans",sans-serif;color:var(--ink)}
.title{position:absolute;top:11px;left:13px;font:600 5.4px "Montserrat",sans-serif;color:var(--ink)}
.brand{position:absolute;top:7px;right:11px;display:flex;flex-direction:column;align-items:center;gap:1.5px;font:600 3.4px "Montserrat",sans-serif;color:var(--navy)}
.brand i{display:block;width:7px;height:7px;background:var(--navy)}
.url{position:absolute;bottom:6px;left:13px;font:600 2.6px "Montserrat",sans-serif;color:var(--ink)}
.pg{position:absolute;bottom:5px;right:10px;width:5px;height:5px;border:.4px solid var(--grey-light);border-radius:50%}
.tx{font:400 2.6px/1.55 "Open Sans",sans-serif;color:var(--muted)}
.t{font:600 3.3px/1.3 "Montserrat",sans-serif;color:var(--navy)}
.t.gold{color:var(--gold)}
.t.grey{color:var(--grey)}
.ic{width:9px;height:9px;border-radius:50%;background:var(--navy);display:grid;place-items:center;flex:none;color:var(--white);font:700 3.4px "Montserrat",sans-serif}
.ic svg{width:5px;height:5px;fill:var(--white)}
.ic.gold{background:var(--gold)}
.ic.grey{background:var(--grey)}
.ph{position:absolute;display:block}
.ph-building{background:linear-gradient(160deg,#d9e2ea 0%,#aab5c0 55%,#7f8a94 100%)}
.ph-people{background:linear-gradient(180deg,#e9edf0 0%,#b9c0c7 45%,#3b4254 100%)}
.ph-digital{background:linear-gradient(135deg,#e8f3fb 0%,#7fb6df 50%,#1f3d6b 100%)}
.ph-interior{background:linear-gradient(170deg,#eef0f2 0%,#c9ccd0 55%,#8f959c 100%)}
.row{display:flex;align-items:center;gap:3px}
ul.bul{list-style:none}
ul.bul li{position:relative;padding-left:4px;font:400 2.6px/1.6 "Open Sans",sans-serif;color:var(--muted)}
ul.bul li::before{content:"";position:absolute;left:0;top:1.3px;width:1.5px;height:1.5px;border-radius:50%;background:var(--gold)}

/* cover */
.cover .ph{inset:0}
.cover-card{position:absolute;left:66px;top:16px;width:114px;height:104px;background:rgba(255,255,255,.55);display:flex;flex-direction:column;align-items:center;text-align:center;padding-top:8px}
.cover-card .mark{width:14px;height:14px;background:var(--navy)}
.cover-name{font:600 6px "Montserrat",sans-serif;color:var(--navy);margin-top:3px}
.cover-title{font:700 5px "Montserrat",sans-serif;color:var(--ink);margin:3px 0 3px}
.cover-card .tx{color:#555;padding:0 6px}
.dots{display:flex;gap:1.5px;margin-top:4px}
.dots b{width:2px;height:2px;border-radius:50%;background:var(--ink)}

/* single image */
.single .ph{inset:0;background:linear-gradient(160deg,#3a4a6a 0%,#22304f 60%,#1a2540 100%)}
.single-body{position:absolute;inset:0;display:flex;flex-direction:column;align-items:center;justify-content:center;text-align:center;color:var(--white);padding:0 28px}
.single-body svg{width:6px;height:6px;fill:var(--white)}
.single-body h2{font:400 6px "Montserrat",sans-serif;margin:4px 0 5px}
.single-body .tx{color:#c5cbd6}

/* points */
.points{position:absolute;top:32px;left:24px;right:14px;display:flex;flex-direction:column;gap:6px}
.points li{list-style:none;display:flex;gap:6px;align-items:flex-start}
.chev{width:27px;height:13px;flex:none}
.chev .shape{fill:var(--navy)}
.chev.gold .shape{fill:var(--gold)}
.chev .glyph{fill:var(--white)}

.timeline,.chart{position:absolute;left:0;top:0;width:246px;height:141px}
.chart text{font-family:"Open Sans",sans-serif}

.grid3{position:absolute;top:36px;left:16px;right:16px;display:grid;grid-template-columns:repeat(3,1fr);column-gap:10px;row-gap:12px}
.grid3 .tx{margin-top:3px}
.grid2{position:absolute;top:32px;left:28px;right:20px;display:grid;grid-template-columns:1fr 1fr;column-gap:14px;row-gap:8px}
.grid2 .row{align-items:flex-start}
.sub{font:600 2.6px "Open Sans",sans-serif;color:var(--ink)}

.partners{position:absolute;top:30px;left:18px;right:18px;display:grid;grid-template-columns:repeat(4,1fr);gap:8px;text-align:center}
.badge{display:block;width:24px;height:24px;border-radius:50%;margin:0 auto 4px;background:#e9ebef;border:1.2px solid var(--navy)}
.badge.gold{border-color:var(--gold)}
.partners .role{font:400 2.4px "Open Sans",sans-serif;color:var(--muted)}
.partners hr{border:0;border-top:.5px solid var(--navy);width:10px;margin:3px auto}

.cols3{position:absolute;top:30px;left:18px;right:16px;display:grid;grid-template-columns:repeat(3,1fr);gap:12px}
.cols3 .tx{margin:4px 0 2px}

.cols4{position:absolute;left:14px;right:14px;display:grid;grid-template-columns:repeat(4,1fr);gap:8px;text-align:center}
.big{width:20px;height:20px;border-radius:50%;background:var(--navy);margin:0 auto 5px;display:grid;place-items:center;box-shadow:0 0 0 2px #e9ebef}
.big svg{width:9px;height:9px;fill:var(--white)}
.big.gold{background:var(--gold);box-shadow:0 0 0 2px #fbe7c2}
.cols4 .t{font-weight:400;color:var(--grey);margin-bottom:3px}
.cols4 .t.gold{color:var(--gold)}
.cols4 .t.strong{color:var(--navy);font-weight:600}

.ring{width:32px;height:32px;margin:0 auto 5px;display:block}
.btn{display:inline-block;margin-top:4px;padding:1px 6px;border-radius:4px;background:var(--navy);color:var(--white);font:600 2.3px "Montserrat",sans-serif}
.btn.gold{background:var(--gold)}

.two-col{position:absolute;top:27px;left:18px;right:18px;display:grid;grid-template-columns:1fr 1fr;gap:12px}
.two-col .tx{margin-bottom:3px}

.photo-caption .ph{left:12px;right:12px;top:0;height:112px}
.photo-caption .tx{position:absolute;left:22px;right:22px;top:114px;text-align:center}

.checker{position:absolute;left:0;right:0;top:8px;height:110px;display:grid;grid-template-columns:repeat(5,1fr);grid-template-rows:1fr 1fr}
.checker div{padding:4px;text-align:center}
.checker .y{background:var(--gold)}
.checker .n{background:var(--navy)}
.checker .g{background:#e2e3e5}
.checker .t{color:var(--white);font-size:2.8px;margin-bottom:2px}
.checker .tx{color:rgba(255,255,255,.85);font-size:2.2px}
.checker-note{position:absolute;left:18px;right:14px;top:120px}

.split .ph{left:0;top:0;bottom:0;width:118px}
.split-body{position:absolute;left:128px;right:12px;top:20px}
.split-body .lead{margin:2px 0 5px}
.split-body .row{align-items:flex-start;margin-bottom:4px}
.ic.sm{width:7px;height:7px}
.ic.sm svg{width:4px;height:4px}

.port4{position:absolute;top:34px;left:16px;right:16px;display:grid;grid-template-columns:repeat(4,1fr);gap:5px}
.port4 .img{position:relative;height:68px;margin-bottom:3px}
.port4 .img .ph{inset:0}

.thumbs{position:absolute;top:32px;left:16px;right:16px;display:grid;grid-template-columns:repeat(4,1fr);gap:5px 8px}
.thumbs .img{position:relative;height:24px;margin-bottom:2px}
.thumbs .img .ph{inset:0}
.thumbs .tx{font-size:2.2px;line-height:1.3;color:var(--ink)}

.device{position:absolute;background:#1b1d22;border-radius:3px}
.device .ph{inset:3px}
.tablet-body{position:absolute;left:102px;right:14px;top:34px}
.icon-list{display:grid;grid-template-columns:1fr 1fr;gap:4px 8px;margin-top:5px}
.icon-list .row{align-items:flex-start}
.icon-list .t{font-size:2.6px}
.feat-row{display:flex;gap:8px;margin-top:5px}
.feat-row div{text-align:center}
.feat-row .ic{margin:0 auto 2px}
.feat-row .t{font-size:2.4px}

/* business case table */
.calc{position:absolute;top:30px;left:22px;width:202px;border-collapse:collapse;font:400 2.7px "Open Sans",sans-serif;color:var(--ink)}
.calc th{height:12px;font:600 2.5px "Montserrat",sans-serif;color:var(--white);padding:1px 2px;text-align:right}
.calc th.label{background:var(--white);color:var(--ink);font-size:3.4px;text-align:left;line-height:1.2}
.calc th.c1,.calc th.c2{background:var(--grey)}
.calc th.c3{background:var(--navy)}
.calc th.c4{background:var(--gold)}
.calc td{height:10px;border-bottom:.4px solid #e3e4e6;text-align:right;padding:0 3px}
.calc td:first-child{text-align:left;padding-left:3px;background:#f4f4f5;color:var(--muted)}
.calc tr.total td{font-weight:600;color:var(--navy)}
.calc tr.total td:last-child{color:var(--gold)}
.calc-note{position:absolute;left:22px;right:22px;top:108px}

.desk .ph{left:100px;top:36px;width:104px;height:86px}
.tag{position:absolute;background:var(--navy);color:var(--white);font:400 2.6px "Open Sans",sans-serif;padding:2px 5px}

.legend{position:absolute;right:14px;top:50px;width:50px;display:flex;flex-direction:column;gap:4px}
.legend .row{align-items:flex-start}
.legend .t{font-size:2.6px}

.tile-list{position:absolute;left:20px;top:28px;width:100px}
.tile-list .row{align-items:flex-start;margin-top:4px}
.tile-list .t{font-size:2.6px}
.tile .ph{left:130px;top:32px;width:48px;height:94px}
.tile-quote{position:absolute;left:178px;top:32px;width:48px;height:46px;background:var(--navy);display:grid;place-items:center}
.tile-quote svg{width:16px;height:16px;fill:var(--white)}
.tile-gold{position:absolute;left:178px;top:78px;width:48px;height:48px;background:var(--gold);padding:5px 4px}
.tile-gold .tx{color:var(--white);font-size:2.2px}

.contact .ph{left:0;right:0;top:0;height:99px}
.addr{position:absolute;left:106px;top:28px;width:46px;background:var(--white);padding:3px;font:400 2.4px/1.4 "Open Sans",sans-serif;color:var(--ink)}
.contact-bar{position:absolute;left:0;right:0;top:99px;bottom:0;display:flex;align-items:center;gap:12px;padding-left:26px}
.contact-bar h3{font:700 6px "Montserrat",sans-serif;color:var(--navy);margin-right:20px}
.contact-bar .ic{width:10px;height:10px;background:var(--white);border:.7px solid var(--navy)}
.contact-bar .ic svg{fill:var(--navy)}
.contact-bar .ic.gold{border-color:var(--gold)}
.contact-bar .ic.gold svg{fill:var(--gold)}
.contact-bar b{display:block;font:600 3.4px "Montserrat",sans-serif;color:var(--navy)}
.contact-bar b.gold{color:var(--gold)}
.contact-bar span{font:400 2.3px "Open Sans",sans-serif;color:var(--ink)}
.sprite{position:absolute;width:0;height:0}
</style>
</head>
<body>
<svg class="sprite" aria-hidden="true">
  <defs>
    <symbol id="i-screen" viewBox="0 0 16 16"><path d="M1 2h14v9H1zM6 12h4v2H6z"/></symbol>
    <symbol id="i-rocket" viewBox="0 0 16 16"><path d="M15 1L6 5 2 6l3 3 2 3 1-4 7-7zM2 11l-1 4 4-1z"/></symbol>
    <symbol id="i-quote" viewBox="0 0 16 16"><path d="M1 3h6v6l-3 5H2l2-5H1zM9 3h6v6l-3 5h-2l2-5H9z"/></symbol>
    <symbol id="i-shield" viewBox="0 0 16 16"><path d="M8 1l6 2v5c0 4-3 6-6 7-3-1-6-3-6-7V3z"/></symbol>
    <symbol id="i-check" viewBox="0 0 16 16"><path d="M1 8l2-2 3 3 7-7 2 2-9 9z"/></symbol>
    <symbol id="i-ring" viewBox="0 0 16 16"><path fill-rule="evenodd" d="M8 1a7 7 0 1 0 .01 0zM8 5a3 3 0 1 1-.01 0z"/></symbol>
    <symbol id="i-user" viewBox="0 0 16 16"><circle cx="8" cy="5" r="3.5"/><path d="M1 15c0-4 3-6 7-6s7 2 7 6z"/></symbol>
    <symbol id="i-home" viewBox="0 0 16 16"><path d="M8 1l7 6h-2v8H3V7H1z"/></symbol>
    <symbol id="i-mail" viewBox="0 0 16 16"><path d="M1 3h14v10H1zM2 4l6 5 6-5z" fill-rule="evenodd"/></symbol>
    <symbol id="i-phone" viewBox="0 0 16 16"><path d="M4 1l3 4-2 2c1 2 2 3 4 4l2-2 4 3-2 3C7 15 1 9 1 3z"/></symbol>
  </defs>
</svg>

<main class="board">

  <!-- 1 cover -->
  <section class="slide cover">
    <div class="ph ph-building" role="img" aria-label="Faded photo of the company building carrying the company sign"></div>
    <div class="cover-card">
      <span class="mark"></span>
      <p class="cover-name">Brevik Hamna</p>
      <p class="cover-title">Welcome Message</p>
      <p class="tx">A short welcome line for the meeting goes here. Keep it friendly, clear and easy to read for every guest in the room today.</p>
      <div class="dots"><b></b><b></b><b></b></div>
    </div>
  </section>

  <!-- 2 single image -->
  <section class="slide single">
    <div class="ph" role="img" aria-label="Building facade photo under a navy overlay"></div>
    <div class="single-body">
      <svg viewBox="0 0 16 16"><use href="#i-quote"/></svg>
      <h2>Creative Single Image Portfolio Options</h2>
      <p class="tx">Place one strong image here and add a short line of text that explains the idea behind it for your audience in a few words.</p>
    </div>
  </section>

  <!-- 3 points -->
  <section class="slide">
    <h1 class="title">Point Visual Design</h1>
    <div class="brand"><i></i>Brevik Hamna</div>
    <ul class="points">
      <li><svg class="chev" viewBox="0 0 27 13"><path class="shape" d="M0 0h22l5 6.5-5 6.5H0l4-6.5z"/><use class="glyph" href="#i-screen" x="10" y="3" width="7" height="7"/></svg><div><p class="t">Creative Strategy</p><p class="tx">Write a short note about this point here and keep it to two simple lines of text for the slide.</p></div></li>
      <li><svg class="chev" viewBox="0 0 27 13"><path class="shape" d="M0 0h22l5 6.5-5 6.5H0l4-6.5z"/><use class="glyph" href="#i-rocket" x="10" y="3" width="7" height="7"/></svg><div><p class="t">Boost Sales</p><p class="tx">Write a short note about this point here and keep it to two simple lines of text for the slide.</p></div></li>
      <li><svg class="chev" viewBox="0 0 27 13"><path class="shape" d="M0 0h22l5 6.5-5 6.5H0l4-6.5z"/><use class="glyph" href="#i-quote" x="10" y="3" width="7" height="7"/></svg><div><p class="t">Global Brand Strategy</p><p class="tx">Write a short note about this point here and keep it to two simple lines of text for the slide.</p></div></li>
      <li><svg class="chev gold" viewBox="0 0 27 13"><path class="shape" d="M0 0h22l5 6.5-5 6.5H0l4-6.5z"/><use class="glyph" href="#i-shield" x="10" y="3" width="7" height="7"/></svg><div><p class="t">Business Strategy</p><p class="tx">Write a short note about this point here and keep it to two simple lines of text for the slide.</p></div></li>
    </ul>
    <p class="url">www.brevikhamna.se</p><span class="pg"></span>
  </section>

  <!-- 4 project timeline -->
  <section class="slide">
    <h1 class="title">Project Timeline</h1>
    <div class="brand"><i></i>Brevik Hamna</div>
    <svg class="timeline" viewBox="0 0 246 141">
      <line x1="20" y1="75" x2="228" y2="75" stroke="#f7b12e" stroke-width=".8"/>
      <g fill="#1e2b48" font-family="Montserrat" font-size="2.6" font-weight="600" text-anchor="middle">
        <text x="27" y="33">Project</text><text x="27" y="36.5">Start</text>
        <text x="110" y="33">Building</text><text x="110" y="36.5">Permit</text>
        <text x="200" y="33">Construction</text><text x="200" y="36.5">Complete</text>
        <text x="92" y="68">Q1 2025</text><text x="173" y="68">Q3 2026</text>
      </g>
      <g stroke="#1e2b48" stroke-width=".6">
        <line x1="27" y1="55" x2="27" y2="75"/><line x1="110" y1="55" x2="110" y2="75"/><line x1="200" y1="55" x2="200" y2="75"/>
      </g>
      <g stroke="#f7b12e" stroke-width=".6">
        <line x1="55" y1="75" x2="55" y2="91"/><line x1="140" y1="75" x2="140" y2="91"/><line x1="221" y1="75" x2="221" y2="91"/>
      </g>
      <circle cx="27" cy="49" r="6" fill="#1e2b48"/><use href="#i-user" x="24.5" y="46.5" width="5" height="5" fill="#fff"/>
      <circle cx="110" cy="49" r="6" fill="#1e2b48"/><use href="#i-check" x="107.5" y="46.5" width="5" height="5" fill="#fff"/>
      <circle cx="200" cy="49" r="6" fill="#1e2b48"/><use href="#i-home" x="197.5" y="46.5" width="5" height="5" fill="#fff"/>
      <path d="M90 72h4v3h-4zM171 72h4v3h-4z" fill="#1e2b48"/>
      <circle cx="55" cy="97" r="6" fill="#f7b12e"/><use href="#i-quote" x="52.5" y="94.5" width="5" height="5" fill="#fff"/>
      <circle cx="140" cy="97" r="6" fill="#f7b12e"/><use href="#i-rocket" x="137.5" y="94.5" width="5" height="5" fill="#fff"/>
      <circle cx="221" cy="97" r="6" fill="#f7b12e"/><use href="#i-shield" x="218.5" y="94.5" width="5" height="5" fill="#fff"/>
      <g fill="#1e2b48" font-family="Montserrat" font-size="2.6" font-weight="600" text-anchor="middle">
        <text x="55" y="110">Financing</text><text x="55" y="113.5">Agreed</text>
        <text x="140" y="110">Construction</text><text x="140" y="113.5">Start</text>
        <text x="221" y="110">Tenants</text><text x="221" y="113.5">Move In</text>
      </g>
    </svg>
    <p class="url">www.brevikhamna.se</p><span class="pg"></span>
  </section>

  <!-- 5 table of contents -->
  <section class="slide">
    <h1 class="title">Table of Contents</h1>
    <div class="brand"><i></i>Brevik Hamna</div>
    <div class="grid3">
      <div><div class="row"><span class="ic">1</span><span class="t">Company Introduction</span></div><p class="tx">Who we are, our history and the harbour site in brief.</p></div>
      <div><div class="row"><span class="ic">2</span><span class="t">Project Timeline</span></div><p class="tx">Key milestones from planning to tenant move in.</p></div>
      <div><div class="row"><span class="ic">3</span><span class="t">Business Case</span></div><p class="tx">Investment, income, costs and expected yield.</p></div>
      <div><div class="row"><span class="ic">4</span><span class="t">Our Buildings</span></div><p class="tx">Offices, warehouse and workshop in short facts.</p></div>
      <div><div class="row"><span class="ic">5</span><span class="t">Inspiration</span></div><p class="tx">Exterior, upper floor and lower floor pictures.</p></div>
      <div><div class="row"><span class="ic gold">6</span><span class="t">Business Partners</span></div><p class="tx">The partners who stand behind the project.</p></div>
    </div>
    <p class="url">www.brevikhamna.se</p><span class="pg"></span>
  </section>

  <!-- 6 bullet list -->
  <section class="slide">
    <h1 class="title">Bullet List Example</h1>
    <div class="brand"><i></i>Brevik Hamna</div>
    <div class="grid2">
      <div class="row"><span class="ic"><svg><use href="#i-check"/></svg></span><div><p class="t">First Main Point</p><p class="sub">A short bold summary line here</p><p class="tx">Add two short lines of supporting text for this item.</p></div></div>
      <div class="row"><span class="ic"><svg><use href="#i-check"/></svg></span><div><p class="t">Second Main Point</p><p class="sub">A short bold summary line here</p><p class="tx">Add two short lines of supporting text for this item.</p></div></div>
      <div class="row"><span class="ic"><svg><use href="#i-check"/></svg></span><div><p class="t">Third Main Point</p><p class="sub">A short bold summary line here</p><p class="tx">Add two short lines of supporting text for this item.</p></div></div>
      <div class="row"><span class="ic"><svg><use href="#i-check"/></svg></span><div><p class="t">Fourth Main Point</p><p class="sub">A short bold summary line here</p><p class="tx">Add two short lines of supporting text for this item.</p></div></div>
      <div class="row"><span class="ic"><svg><use href="#i-check"/></svg></span><div><p class="t">Fifth Main Point</p><p class="sub">A short bold summary line here</p><p class="tx">Add two short lines of supporting text for this item.</p></div></div>
      <div class="row"><span class="ic"><svg><use href="#i-check"/></svg></span><div><p class="t">Sixth Main Point</p><p class="sub">A short bold summary line here</p><p class="tx">Add two short lines of supporting text for this item.</p></div></div>
    </div>
    <p class="url">www.brevikhamna.se</p><span class="pg"></span>
  </section>

  <!-- 7 business partners -->
  <section class="slide">
    <h1 class="title">Our Business Partners</h1>
    <div class="brand"><i></i>Brevik Hamna</div>
    <div class="partners">
      <div><span class="badge"></span><p class="t">Nordvik Bank</p><p class="role">Financing Partner</p><hr><p class="tx">Long term partner for the financing of the project.</p></div>
      <div><span class="badge"></span><p class="t">Kustbygg AB</p><p class="role">Construction Partner</p><hr><p class="tx">Main contractor for the new harbour buildings.</p></div>
      <div><span class="badge"></span><p class="t">Hällberg Arkitekter</p><p class="role">Architect</p><hr><p class="tx">Design of facades, floor plans and interiors.</p></div>
      <div><span class="badge gold"></span><p class="t">Sundfast Förvaltning</p><p class="role">Property Manager</p><hr><p class="tx">Daily operation and care of the buildings.</p></div>
    </div>
    <p class="url">www.brevikhamna.se</p><span class="pg"></span>
  </section>

  <!-- 8 our buildings -->
  <section class="slide">
    <h1 class="title">Our Buildings</h1>
    <div class="brand"><i></i>Brevik Hamna</div>
    <div class="cols3">
      <div><div class="row"><span class="ic"><svg><use href="#i-home"/></svg></span><span class="t">Building A – Offices</span></div><p class="tx">Modern office space facing the harbour.</p>
        <ul class="bul"><li>2 400 m² over two floors</li><li>Open plan and meeting rooms</li><li>Built in 2019, renovated 2024</li><li>Parking for 60 cars</li></ul></div>
      <div><div class="row"><span class="ic"><svg><use href="#i-home"/></svg></span><span class="t">Building B – Warehouse</span></div><p class="tx">Flexible storage close to the quay.</p>
        <ul class="bul"><li>5 100 m² floor area</li><li>Free height of 8 metres</li><li>Six loading docks</li><li>Direct access to the main road</li></ul></div>
      <div><div class="row"><span class="ic gold"><svg><use href="#i-home"/></svg></span><span class="t">Building C – Workshop</span></div><p class="tx">Light industry with office on the upper floor.</p>
        <ul class="bul"><li>1 800 m² workshop hall</li><li>400 m² office upper floor</li><li>Overhead crane 10 tonnes</li><li>Ready for new tenants 2026</li></ul></div>
    </div>
    <p class="url">www.brevikhamna.se</p><span class="pg"></span>
  </section>

  <!-- 9 four circles -->
  <section class="slide">
    <h1 class="title">Creative Visual Design</h1>
    <div class="brand"><i></i>Brevik Hamna</div>
    <div class="cols4" style="top:38px">
      <div><span class="big"><svg><use href="#i-screen"/></svg></span><p class="t">Desktop Application</p><p class="tx">Short notes for this item go here in a few lines of plain text.</p></div>
      <div><span class="big"><svg><use href="#i-ring"/></svg></span><p class="t">Business Strategy</p><p class="tx">Short notes for this item go here in a few lines of plain text.</p></div>
      <div><span class="big"><svg><use href="#i-shield"/></svg></span><p class="t strong">Sales Booster</p><p class="tx">Short notes for this item go here in a few lines of plain text.</p></div>
      <div><span class="big gold"><svg><use href="#i-rocket"/></svg></span><p class="t gold">Concept &amp; Ideas</p><p class="tx">Short notes for this item go here in a few lines of plain text.</p></div>
    </div>
    <p class="url">www.brevikhamna.se</p><span class="pg"></span>
  </section>

  <!-- 10 progress rings -->
  <section class="slide">
    <h1 class="title">Creative Visual Design</h1>
    <div class="brand"><i></i>Brevik Hamna</div>
    <div class="cols4" style="top:30px">
      <div><svg class="ring" viewBox="0 0 36 36"><circle cx="18" cy="18" r="15" fill="none" stroke="#e4e5e8" stroke-width="2"/><circle cx="18" cy="18" r="15" fill="none" stroke="#1e2b48" stroke-width="2.4" stroke-dasharray="23.6 94.2" transform="rotate(-90 18 18)"/><text x="18" y="20.5" text-anchor="middle" font-family="Montserrat" font-weight="700" font-size="7" fill="#1e2b48">25%</text></svg><p class="t">Desktop Application</p><p class="tx">A short line of text for this item here.</p><span class="btn">LAUNCH</span></div>
      <div><svg class="ring" viewBox="0 0 36 36"><circle cx="18" cy="18" r="15" fill="none" stroke="#e4e5e8" stroke-width="2"/><circle cx="18" cy="18" r="15" fill="none" stroke="#1e2b48" stroke-width="2.4" stroke-dasharray="65 94.2" transform="rotate(-90 18 18)"/><text x="18" y="20.5" text-anchor="middle" font-family="Montserrat" font-weight="700" font-size="7" fill="#1e2b48">69%</text></svg><p class="t">Desktop Application</p><p class="tx">A short line of text for this item here.</p><span class="btn">LAUNCH</span></div>
      <div><svg class="ring" viewBox="0 0 36 36"><circle cx="18" cy="18" r="15" fill="none" stroke="#e4e5e8" stroke-width="2"/><circle cx="18" cy="18" r="15" fill="none" stroke="#1e2b48" stroke-width="2.4" stroke-dasharray="37.7 94.2" transform="rotate(-90 18 18)"/><text x="18" y="20.5" text-anchor="middle" font-family="Montserrat" font-weight="700" font-size="7" fill="#1e2b48">40%</text></svg><p class="t strong">Desktop Application</p><p class="tx">A short line of text for this item here.</p><span class="btn">LAUNCH</span></div>
      <div><svg class="ring" viewBox="0 0 36 36"><circle cx="18" cy="18" r="15" fill="none" stroke="#fbe7c2" stroke-width="2"/><circle cx="18" cy="18" r="15" fill="none" stroke="#f7b12e" stroke-width="2.4" stroke-dasharray="65 94.2" transform="rotate(-90 18 18)"/><text x="18" y="20.5" text-anchor="middle" font-family="Montserrat" font-weight="700" font-size="7" fill="#f7b12e">69%</text></svg><p class="t gold">Desktop Application</p><p class="tx">A short line of text for this item here.</p><span class="btn gold">LAUNCH</span></div>
    </div>
    <p class="url">www.brevikhamna.se</p><span class="pg"></span>
  </section>

  <!-- 11 two column text -->
  <section class="slide">
    <h1 class="title">Two Column Text</h1>
    <div class="brand"><i></i>Brevik Hamna</div>
    <div class="two-col">
      <div>
        <p class="tx">Open this column with a short summary of the topic. Keep the tone formal and clear for the reader.</p>
        <p class="tx">Add supporting detail in this paragraph. Explain the main facts, the key numbers and the reasons behind them in a few calm sentences that are easy to follow during a meeting.</p>
        <p class="tx">Close the column with a short line that leads into the next part of the slide and the next point of the talk.</p>
      </div>
      <div>
        <p class="tx">Open this column with a short summary of the topic. Keep the tone formal and clear for the reader.</p>
        <p class="tx">Add supporting detail in this paragraph. Explain the main facts, the key numbers and the reasons behind them in a few calm sentences that are easy to follow during a meeting.</p>
        <p class="tx">Close the column with a short line that leads into the next part of the slide and the next point of the talk.</p>
      </div>
    </div>
    <p class="url">www.brevikhamna.se</p><span class="pg"></span>
  </section>

  <!-- 12 full photo -->
  <section class="slide photo-caption">
    <div class="ph ph-people" role="img" aria-label="Group photo of the business team in suits"></div>
    <p class="tx">Add a short caption for the team photo here. Two lines are enough to explain who is shown and why it matters for this meeting.</p>
    <span class="pg"></span>
  </section>

  <!-- 13 checker -->
  <section class="slide">
    <div class="checker">
      <div class="g"></div>
      <div class="y"><p class="t">Portfolio Two</p><p class="tx">Short note for this block here.</p></div>
      <div class="g"></div>
      <div class="y"><p class="t">Portfolio Four</p><p class="tx">Short note for this block here.</p></div>
      <div class="g"></div>
      <div class="n"><p class="t">Portfolio One</p><p class="tx">Short note for this block here.</p></div>
      <div class="g"></div>
      <div class="n"><p class="t">Portfolio Three</p><p class="tx">Short note for this block here.</p></div>
      <div class="g"></div>
      <div class="n"><p class="t">Portfolio Five</p><p class="tx">Short note for this block here.</p></div>
    </div>
    <p class="tx checker-note">Add one short line of text under the portfolio blocks to explain the set of projects shown above here.</p>
    <p class="url">www.brevikhamna.se</p><span class="pg"></span>
  </section>

  <!-- 14 project detail -->
  <section class="slide split">
    <div class="ph ph-digital" role="img" aria-label="Business person touching a digital interface"></div>
    <div class="split-body">
      <p class="t" style="color:var(--ink);font-size:4px">Project Detail</p>
      <p class="tx lead">Give a short overview of the project here in two or three brief lines.</p>
      <div class="row"><span class="ic sm"><svg><use href="#i-screen"/></svg></span><div><p class="t">Desktop Application</p><p class="tx">Two short lines of text that describe this part of the work.</p></div></div>
      <div class="row"><span class="ic sm"><svg><use href="#i-ring"/></svg></span><div><p class="t">Creative Strategy</p><p class="tx">Two short lines of text that describe this part of the work.</p></div></div>
      <div class="row"><span class="ic sm gold"><svg><use href="#i-shield"/></svg></span><div><p class="t gold">System Security</p><p class="tx">Two short lines of text that describe this part of the work.</p></div></div>
    </div>
    <span class="pg"></span>
  </section>

  <!-- 15 exterior pictures -->
  <section class="slide">
    <h1 class="title">Inspiration – Exterior</h1>
    <div class="brand"><i></i>Brevik Hamna</div>
    <div class="port4">
      <div><div class="img"><span class="ph ph-building" role="img" aria-label="Photo of a building corner with wooden cladding"></span></div><p class="t">Facade Detail</p><p class="tx">Wood and steel meet at the entrance.</p></div>
      <div><div class="img"><span class="ph ph-building" role="img" aria-label="Photo of the office building exterior"></span></div><p class="t">Main Entrance</p><p class="tx">A clear, welcoming front to the quay.</p></div>
      <div><div class="img"><span class="ph ph-building" role="img" aria-label="Photo of the building facade and car park"></span></div><p class="t">Car Park</p><p class="tx">Parking close to every building.</p></div>
      <div><div class="img"><span class="ph ph-building" role="img" aria-label="Photo of the building under a blue sky"></span></div><p class="t">Long Facade</p><p class="tx">Calm lines along the harbour road.</p></div>
    </div>
    <p class="url">www.brevikhamna.se</p><span class="pg"></span>
  </section>

  <!-- 16 interior upper floor -->
  <section class="slide">
    <h1 class="title">INTERIOR UPPER FLOOR</h1>
    <div class="brand"><i></i>Brevik Hamna</div>
    <div class="thumbs">
      <div><div class="img"><span class="ph ph-interior" role="img" aria-label="Photo of an open plan office"></span></div><p class="tx">Open Office<br>Upper floor</p></div>
      <div><div class="img"><span class="ph ph-interior" role="img" aria-label="Photo of a meeting room"></span></div><p class="tx">Meeting Room<br>Upper floor</p></div>
      <div><div class="img"><span class="ph ph-interior" role="img" aria-label="Photo of a staff kitchen"></span></div><p class="tx">Kitchen<br>Upper floor</p></div>
      <div><div class="img"><span class="ph ph-interior" role="img" aria-label="Photo of a reception area"></span></div><p class="tx">Reception<br>Upper floor</p></div>
      <div><div class="img"><span class="ph ph-interior" role="img" aria-label="Photo of a lounge"></span></div><p class="tx">Lounge<br>Upper floor</p></div>
      <div><div class="img"><span class="ph ph-interior" role="img" aria-label="Photo of a private office"></span></div><p class="tx">Private Office<br>Upper floor</p></div>
      <div><div class="img"><span class="ph ph-interior" role="img" aria-label="Photo of a corridor with glass walls"></span></div><p class="tx">Corridor<br>Upper floor</p></div>
      <div><div class="img"><span class="ph ph-interior" role="img" aria-label="Photo of a roof terrace"></span></div><p class="tx">Terrace<br>Upper floor</p></div>
    </div>
    <p class="url">www.brevikhamna.se</p><span class="pg"></span>
  </section>

  <!-- 17 tablet smartphone -->
  <section class="slide">
    <h1 class="title">Creative Tablet Smartphone Data</h1>
    <div class="brand"><i></i>Brevik Hamna</div>
    <div class="device" style="left:26px;top:38px;width:54px;height:72px"><span class="ph ph-people" role="img" aria-label="Tablet screen showing a business portrait"></span></div>
    <div class="device" style="left:74px;top:58px;width:22px;height:40px"><span class="ph ph-digital" style="inset:3px 2px" role="img" aria-label="Phone screen showing a digital interface"></span></div>
    <div class="tablet-body">
      <p class="t" style="color:var(--ink)">Mobile Data Analysis</p>
      <p class="tx">Give a short summary of the mobile data here in two or three brief lines.</p>
      <div class="icon-list">
        <div class="row"><span class="ic sm"><svg><use href="#i-screen"/></svg></span><div><p class="t">Desktop Application</p><p class="tx">A short note here.</p></div></div>
        <div class="row"><span class="ic sm"><svg><use href="#i-user"/></svg></span><div><p class="t">Meeting Strategy</p><p class="tx">A short note here.</p></div></div>
        <div class="row"><span class="ic sm"><svg><use href="#i-quote"/></svg></span><div><p class="t">Sales Chart Data</p><p class="tx">A short note here.</p></div></div>
        <div class="row"><span class="ic sm"><svg><use href="#i-ring"/></svg></span><div><p class="t">Concept &amp; Idea</p><p class="tx">A short note here.</p></div></div>
        <div class="row"><span class="ic sm gold"><svg><use href="#i-shield"/></svg></span><div><p class="t">Content Strategy</p><p class="tx">A short note here.</p></div></div>
        <div class="row"><span class="ic sm gold"><svg><use href="#i-rocket"/></svg></span><div><p class="t">Launch Application</p><p class="tx">A short note here.</p></div></div>
      </div>
    </div>
    <p class="url">www.brevikhamna.se</p><span class="pg"></span>
  </section>

  <!-- 18 tablet features -->
  <section class="slide">
    <h1 class="title">Creative Tablet Features</h1>
    <div class="brand"><i></i>Brevik Hamna</div>
    <div style="position:absolute;left:38px;top:38px;width:120px">
      <p class="t" style="color:var(--ink)">Mobile User Data Analysis</p>
      <p class="tx">Use this space for a short paragraph about the user data. Explain the trend in plain words and point out the one result that matters most to the team and partners.</p>
      <div class="feat-row">
        <div><span class="ic"><svg><use href="#i-ring"/></svg></span><p class="t grey">Creative</p></div>
        <div><span class="ic"><svg><use href="#i-screen"/></svg></span><p class="t grey">Message</p></div>
        <div><span class="ic"><svg><use href="#i-user"/></svg></span><p class="t">Management</p></div>
        <div><span class="ic gold"><svg><use href="#i-rocket"/></svg></span><p class="t gold">Marketing</p></div>
      </div>
      <p class="tx" style="margin-top:4px">Add a short closing line about these four features here.</p>
    </div>
    <div class="device" style="left:170px;top:36px;width:52px;height:86px"><span class="ph ph-people" role="img" aria-label="Tablet screen showing a business portrait"></span></div>
    <p class="url">www.brevikhamna.se</p><span class="pg"></span>
  </section>

  <!-- 19 business case -->
  <section class="slide">
    <h1 class="title">Business Case Calculation</h1>
    <div class="brand"><i></i>Brevik Hamna</div>
    <table class="calc">
      <tr><th class="label">Amounts<br>in MSEK</th><th class="c1">2025</th><th class="c2">2026</th><th class="c3">2027</th><th class="c4">2028</th></tr>
      <tr><td>Investment</td><td>-42.0</td><td>-18.5</td><td>-2.0</td><td>-1.5</td></tr>
      <tr><td>Rental income</td><td>3.2</td><td>9.8</td><td>14.6</td><td>15.1</td></tr>
      <tr><td>Operating costs</td><td>-1.1</td><td>-2.9</td><td>-3.8</td><td>-3.9</td></tr>
      <tr><td>Interest costs</td><td>-1.6</td><td>-2.4</td><td>-2.6</td><td>-2.5</td></tr>
      <tr class="total"><td>Net operating result</td><td>0.5</td><td>4.5</td><td>8.2</td><td>8.7</td></tr>
      <tr class="total"><td>Yield on cost</td><td>0.8 %</td><td>5.1 %</td><td>6.4 %</td><td>6.7 %</td></tr>
    </table>
    <p class="tx calc-note">All figures are estimates for discussion. Final numbers follow the signed lease and loan agreements.</p>
    <p class="url">www.brevikhamna.se</p><span class="pg"></span>
  </section>

  <!-- 20 desktop info -->
  <section class="slide desk">
    <h1 class="title">Creative Desktop Info</h1>
    <div class="brand"><i></i>Brevik Hamna</div>
    <div class="ph ph-digital" role="img" aria-label="Business person using a digital screen"></div>
    <span class="tag" style="left:34px;top:57px">Left Navigation</span>
    <span class="tag" style="left:36px;top:100px">Friend List</span>
    <span class="tag" style="left:196px;top:54px">Main Image</span>
    <span class="tag" style="left:196px;top:97px">Music Player</span>
    <p class="url">www.brevikhamna.se</p><span class="pg"></span>
  </section>

  <!-- 21 peaks chart -->
  <section class="slide">
    <h1 class="title">Creative Visual Design</h1>
    <div class="brand"><i></i>Brevik Hamna</div>
    <svg class="chart" viewBox="0 0 246 141">
      <use href="#i-quote" x="24" y="32" width="8" height="8" fill="#1e2b48"/>
      <text x="36" y="35" font-size="2.6" fill="#7b7f86">Write a short quote or note here for this chart.</text>
      <text x="36" y="39" font-size="2.6" fill="#7b7f86">A second line of text can go right here.</text>
      <text x="36" y="44" font-size="2.6" fill="#7b7f86">✓ First short point</text>
      <text x="36" y="48" font-size="2.6" fill="#7b7f86">✓ Second short point</text>
      <text x="36" y="52" font-size="2.6" fill="#7b7f86">✓ Third short point</text>
      <path d="M26 110 Q31 110 33 100 Q35 110 40 110Z" fill="#d4d5d7"/>
      <path d="M36 110 Q42 110 44 98 Q46 110 52 110Z" fill="#c4c6c9"/>
      <path d="M48 110 Q55 110 57 96 Q59 110 66 110Z" fill="#b0b3b7"/>
      <path d="M62 110 Q69 110 71 92 Q73 110 80 110Z" fill="#a0a3a8"/>
      <path d="M76 110 Q83 110 85 89 Q87 110 94 110Z" fill="#8e9196"/>
      <path d="M90 110 Q97 110 99 85 Q101 110 108 110Z" fill="#7a7e84"/>
      <path d="M104 110 Q111 110 113 82 Q115 110 122 110Z" fill="#666b72"/>
      <path d="M118 110 Q125 110 127 78 Q129 110 136 110Z" fill="#4d5260"/>
      <path d="M132 110 Q139 110 141 75 Q143 110 150 110Z" fill="#3a4154"/>
      <path d="M146 110 Q153 110 155 70 Q157 110 164 110Z" fill="#2c3650"/>
      <path d="M160 110 Q167 110 169 66 Q171 110 178 110Z" fill="#1e2b48"/>
      <path d="M174 110 Q181 110 183 62 Q185 110 192 110Z" fill="#1e2b48"/>
      <path d="M188 110 Q195 110 197 58 Q199 110 206 110Z" fill="#f7b12e"/>
      <line x1="22" y1="110" x2="212" y2="110" stroke="#d4d5d7" stroke-width=".5"/>
      <circle cx="33" cy="95" r="3" fill="#d4d5d7"/><text x="33" y="96" font-size="2.2" text-anchor="middle" fill="#fff">1K</text>
      <circle cx="197" cy="51" r="3" fill="#f7b12e"/><text x="197" y="52" font-size="2.2" text-anchor="middle" fill="#fff">9K</text>
      <g font-size="2.2" fill="#7b7f86">
        <circle cx="28" cy="119" r="3" fill="#8e9196"/><text x="33" y="118">Short</text><text x="33" y="121">note</text>
        <circle cx="54" cy="119" r="3" fill="#8e9196"/><text x="59" y="118">Short</text><text x="59" y="121">note</text>
        <circle cx="80" cy="119" r="3" fill="#8e9196"/><text x="85" y="118">Short</text><text x="85" y="121">note</text>
        <circle cx="106" cy="119" r="3" fill="#1e2b48"/><text x="111" y="118">Short</text><text x="111" y="121">note</text>
        <circle cx="132" cy="119" r="3" fill="#1e2b48"/><text x="137" y="118">Short</text><text x="137" y="121">note</text>
        <circle cx="158" cy="119" r="3" fill="#1e2b48"/><text x="163" y="118">Short</text><text x="163" y="121">note</text>
        <circle cx="184" cy="119" r="3" fill="#f7b12e"/><text x="189" y="118">Short</text><text x="189" y="121">note</text>
      </g>
    </svg>
    <p class="url">www.brevikhamna.se</p><span class="pg"></span>
  </section>

  <!-- 22 bar groups -->
  <section class="slide">
    <h1 class="title">Creative Visual Design</h1>
    <div class="brand"><i></i>Brevik Hamna</div>
    <svg class="chart" viewBox="0 0 246 141">
      <g font-size="2.6" fill="#2b2f36" font-weight="600"><text x="40" y="37">Data Series 01</text><text x="105" y="37">Data Series 02</text></g>
      <g font-size="2.2" fill="#7b7f86"><text x="40" y="41">Short note for this series.</text><text x="105" y="41">Short note for this series.</text></g>
      <g stroke="#eceded" stroke-width=".4"><line x1="30" y1="60" x2="160" y2="60"/><line x1="30" y1="75" x2="160" y2="75"/><line x1="30" y1="90" x2="160" y2="90"/><line x1="30" y1="105" x2="160" y2="105"/></g>
      <rect x="50" y="86" width="6" height="33" fill="#8e9196"/><rect x="56" y="68" width="6" height="51" fill="#1e2b48"/><rect x="62" y="76" width="6" height="43" fill="#2b2f36"/><rect x="68" y="102" width="6" height="17" fill="#f7b12e"/>
      <rect x="118" y="96" width="6" height="23" fill="#8e9196"/><rect x="124" y="72" width="6" height="47" fill="#1e2b48"/><rect x="130" y="102" width="6" height="17" fill="#f7b12e"/>
      <line x1="30" y1="119" x2="160" y2="119" stroke="#d4d5d7" stroke-width=".5"/>
      <g font-size="2.2" fill="#7b7f86"><text x="58" y="123">2015</text><text x="124" y="123">2016</text></g>
      <text x="172" y="42" font-size="3" font-weight="600" fill="#2b2f36">Customer Data Analysis</text>
      <g font-size="2.3" fill="#7b7f86"><text x="172" y="47">Write a short note about the</text><text x="172" y="50.5">customer data here in a few</text><text x="172" y="54">brief lines so the chart is easy</text><text x="172" y="57.5">to read for everyone today.</text></g>
      <circle cx="176" cy="78" r="3.5" fill="#1e2b48"/><use href="#i-screen" x="174" y="76" width="4" height="4" fill="#fff"/><text x="181" y="79" font-size="2.4" fill="#1e2b48">Desktop</text>
      <circle cx="200" cy="78" r="3.5" fill="#1e2b48"/><use href="#i-screen" x="198" y="76" width="4" height="4" fill="#fff"/><text x="205" y="79" font-size="2.4" fill="#1e2b48">Notebook</text>
      <circle cx="176" cy="89" r="3.5" fill="#1e2b48"/><use href="#i-screen" x="174" y="87" width="4" height="4" fill="#fff"/><text x="181" y="90" font-size="2.4" fill="#1e2b48">Tablet</text>
      <circle cx="200" cy="89" r="3.5" fill="#f7b12e"/><use href="#i-phone" x="198" y="87" width="4" height="4" fill="#fff"/><text x="205" y="90" font-size="2.4" fill="#f7b12e">Smartphone</text>
    </svg>
    <p class="url">www.brevikhamna.se</p><span class="pg"></span>
  </section>

  <!-- 23 four bar groups -->
  <section class="slide">
    <h1 class="title">Creative Visual Design</h1>
    <div class="brand"><i></i>Brevik Hamna</div>
    <svg class="chart" viewBox="0 0 246 141">
      <g stroke="#eceded" stroke-width=".4"><line x1="26" y1="45" x2="220" y2="45"/><line x1="26" y1="60" x2="220" y2="60"/><line x1="26" y1="75" x2="220" y2="75"/><line x1="26" y1="90" x2="220" y2="90"/></g>
      <rect x="34" y="92" width="5" height="12" fill="#8e9196"/><rect x="39" y="86" width="5" height="18" fill="#2b2f36"/><rect x="44" y="80" width="5" height="24" fill="#1e2b48"/><rect x="49" y="77" width="5" height="27" fill="#f7b12e"/>
      <rect x="82" y="96" width="5" height="8" fill="#8e9196"/><rect x="87" y="94" width="5" height="10" fill="#2b2f36"/><rect x="92" y="96" width="5" height="8" fill="#1e2b48"/><rect x="97" y="95" width="5" height="9" fill="#f7b12e"/>
      <rect x="130" y="86" width="5" height="18" fill="#8e9196"/><rect x="135" y="78" width="5" height="26" fill="#2b2f36"/><rect x="140" y="92" width="5" height="12" fill="#1e2b48"/><rect x="145" y="88" width="5" height="16" fill="#f7b12e"/>
      <rect x="178" y="96" width="5" height="8" fill="#8e9196"/><rect x="183" y="82" width="5" height="22" fill="#1e2b48"/><rect x="188" y="94" width="5" height="10" fill="#2b2f36"/><rect x="193" y="96" width="5" height="8" fill="#f7b12e"/>
      <line x1="26" y1="104" x2="220" y2="104" stroke="#d4d5d7" stroke-width=".5"/>
      <g font-size="2.3">
        <circle cx="32" cy="117" r="4" fill="#8e9196"/><use href="#i-screen" x="29.5" y="114.5" width="5" height="5" fill="#fff"/><text x="38" y="115" font-weight="600" fill="#1e2b48">Number One</text><text x="38" y="118.5" fill="#7b7f86">Short note here</text>
        <circle cx="80" cy="117" r="4" fill="#1e2b48"/><use href="#i-rocket" x="77.5" y="114.5" width="5" height="5" fill="#fff"/><text x="86" y="115" font-weight="600" fill="#1e2b48">Number Two</text><text x="86" y="118.5" fill="#7b7f86">Short note here</text>
        <circle cx="128" cy="117" r="4" fill="#1e2b48"/><use href="#i-quote" x="125.5" y="114.5" width="5" height="5" fill="#fff"/><text x="134" y="115" font-weight="600" fill="#1e2b48">Number Three</text><text x="134" y="118.5" fill="#7b7f86">Short note here</text>
        <circle cx="176" cy="117" r="4" fill="#f7b12e"/><use href="#i-quote" x="173.5" y="114.5" width="5" height="5" fill="#fff"/><text x="182" y="115" font-weight="600" fill="#1e2b48">Number Four</text><text x="182" y="118.5" fill="#7b7f86">Short note here</text>
      </g>
    </svg>
    <p class="url">www.brevikhamna.se</p><span class="pg"></span>
  </section>

  <!-- 24 area chart -->
  <section class="slide">
    <h1 class="title">Creative Visual Design</h1>
    <div class="brand"><i></i>Brevik Hamna</div>
    <svg class="chart" viewBox="0 0 246 141">
      <g stroke="#eceded" stroke-width=".4"><line x1="42" y1="50" x2="176" y2="50"/><line x1="42" y1="65" x2="176" y2="65"/><line x1="42" y1="80" x2="176" y2="80"/><line x1="42" y1="95" x2="176" y2="95"/></g>
      <path d="M42 112 L42 100 L70 70 L100 90 L130 58 L176 80 L176 112Z" fill="#8e9196"/>
      <path d="M42 112 L42 105 L70 92 L100 96 L130 78 L176 98 L176 112Z" fill="#1e2b48"/>
      <path d="M42 112 L75 112 L110 86 L140 100 L176 90 L176 112Z" fill="#f7b12e"/>
      <line x1="42" y1="112" x2="176" y2="112" stroke="#d4d5d7" stroke-width=".5"/>
      <g font-size="2.2" fill="#7b7f86"><text x="40" y="117">2010</text><text x="66" y="117">2011</text><text x="92" y="117">2012</text><text x="118" y="117">2013</text><text x="144" y="117">2014</text></g>
    </svg>
    <div class="legend">
      <div class="row"><span class="ic sm"><svg><use href="#i-screen"/></svg></span><div><p class="t">Type A</p><p class="tx">A short note for this type.</p></div></div>
      <div class="row"><span class="ic sm"><svg><use href="#i-shield"/></svg></span><div><p class="t">Type B</p><p class="tx">A short note for this type.</p></div></div>
      <div class="row"><span class="ic sm"><svg><use href="#i-rocket"/></svg></span><div><p class="t">Type C</p><p class="tx">A short note for this type.</p></div></div>
      <div class="row"><span class="ic sm gold"><svg><use href="#i-quote"/></svg></span><div><p class="t">Type D</p><p class="tx">A short note for this type.</p></div></div>
    </div>
    <p class="url">www.brevikhamna.se</p><span class="pg"></span>
  </section>

  <!-- 25 mind map -->
  <section class="slide">
    <h1 class="title">Creative Visual Design</h1>
    <div class="brand"><i></i>Brevik Hamna</div>
    <svg class="chart" viewBox="0 0 246 141">
      <g fill="none" stroke="#1e2b48" stroke-width=".6">
        <path d="M134 76 H170 V40 H186"/><path d="M170 76 V86 H186"/><path d="M134 80 H160 V112 H186"/>
        <path d="M106 76 H75 V38 H72"/><path d="M75 76 V70 H49"/><path d="M106 80 H85 V106 H72"/>
      </g>
      <circle cx="120" cy="78" r="14" fill="#1e2b48"/>
      <text x="120" y="77" text-anchor="middle" font-size="3.4" fill="#fff" font-family="Montserrat">Business</text>
      <text x="120" y="81.5" text-anchor="middle" font-size="3.4" fill="#fff" font-family="Montserrat">Progam</text>
      <circle cx="68" cy="38" r="3.5" fill="#fff" stroke="#1e2b48" stroke-width=".6"/><use href="#i-ring" x="66" y="36" width="4" height="4" fill="#1e2b48"/>
      <circle cx="45" cy="70" r="3.5" fill="#fff" stroke="#1e2b48" stroke-width=".6"/><use href="#i-ring" x="43" y="68" width="4" height="4" fill="#1e2b48"/>
      <circle cx="68" cy="106" r="3.5" fill="#fff" stroke="#1e2b48" stroke-width=".6"/><use href="#i-ring" x="66" y="104" width="4" height="4" fill="#1e2b48"/>
      <circle cx="190" cy="40" r="3.5" fill="#fff" stroke="#1e2b48" stroke-width=".6"/><use href="#i-screen" x="188" y="38" width="4" height="4" fill="#1e2b48"/>
      <circle cx="190" cy="86" r="3.5" fill="#fff" stroke="#f7b12e" stroke-width=".6"/><use href="#i-quote" x="188" y="84" width="4" height="4" fill="#f7b12e"/>
      <circle cx="190" cy="112" r="3.5" fill="#fff" stroke="#1e2b48" stroke-width=".6"/><use href="#i-screen" x="188" y="110" width="4" height="4" fill="#1e2b48"/>
      <g font-size="2.4" text-anchor="middle">
        <text x="68" y="46" font-weight="600" fill="#1e2b48">Creative Strategy</text><text x="68" y="49.5" fill="#7b7f86">Short note here</text>
        <text x="45" y="78" font-weight="600" fill="#1e2b48">Content Strategy</text><text x="45" y="81.5" fill="#7b7f86">Short note here</text>
        <text x="68" y="114" font-weight="600" fill="#1e2b48">Data Analysis</text><text x="68" y="117.5" fill="#7b7f86">Short note here</text>
        <text x="190" y="48" font-weight="600" fill="#1e2b48">Desktop Application</text><text x="190" y="51.5" fill="#7b7f86">Short note here</text>
        <text x="190" y="94" font-weight="600" fill="#1e2b48">Business Strategy</text><text x="190" y="97.5" fill="#7b7f86">Short note here</text>
        <text x="190" y="120" font-weight="600" fill="#1e2b48">Product Photography</text><text x="190" y="123.5" fill="#7b7f86">Short note here</text>
      </g>
    </svg>
    <p class="url">www.brevikhamna.se</p><span class="pg"></span>
  </section>

  <!-- 26 circles -->
  <section class="slide">
    <h1 class="title">Creative Visual Design</h1>
    <div class="brand"><i></i>Brevik Hamna</div>
    <svg class="chart" viewBox="0 0 246 141">
      <circle cx="44" cy="70" r="21" fill="#a7a9ad"/>
      <circle cx="84" cy="70" r="21" fill="#7e8187"/>
      <circle cx="124" cy="70" r="21" fill="#2b2f36"/>
      <circle cx="164" cy="70" r="21" fill="#1e2b48"/>
      <circle cx="202" cy="70" r="21" fill="#f7b12e"/>
      <use href="#i-screen" x="38" y="64" width="12" height="12" fill="#fff"/>
      <use href="#i-ring" x="78" y="64" width="12" height="12" fill="#fff"/>
      <use href="#i-quote" x="118" y="64" width="12" height="12" fill="#fff"/>
      <use href="#i-shield" x="158" y="64" width="12" height="12" fill="#fff"/>
      <use href="#i-rocket" x="196" y="64" width="12" height="12" fill="#fff"/>
      <g font-size="2.6" text-anchor="middle" font-weight="600" fill="#1e2b48">
        <text x="44" y="101">Website Design</text><text x="84" y="101">Creative Strategy</text><text x="124" y="101">Business Strategy</text><text x="164" y="101">Data Analysis</text><text x="202" y="101">Concept &amp; Idea</text>
      </g>
      <g font-size="2.2" text-anchor="middle" fill="#7b7f86">
        <text x="44" y="105">Short note for this</text><text x="44" y="108">item goes here</text>
        <text x="84" y="105">Short note for this</text><text x="84" y="108">item goes here</text>
        <text x="124" y="105">Short note for this</text><text x="124" y="108">item goes here</text>
        <text x="164" y="105">Short note for this</text><text x="164" y="108">item goes here</text>
        <text x="202" y="105">Short note for this</text><text x="202" y="108">item goes here</text>
      </g>
    </svg>
    <p class="url">www.brevikhamna.se</p><span class="pg"></span>
  </section>

  <!-- 27 lower floor -->
  <section class="slide tile">
    <h1 class="title">Interior Lower Floor</h1>
    <div class="tile-list">
      <p class="t" style="color:var(--ink);font-size:2.8px">Lower Floor Overview</p>
      <p class="tx">A short summary of the lower floor layout and how it is used today.</p>
      <div class="row"><span class="ic sm"><svg><use href="#i-home"/></svg></span><div><p class="t gold">Workshop Hall</p><p class="tx">Large open hall with high ceiling.</p></div></div>
      <div class="row"><span class="ic sm"><svg><use href="#i-user"/></svg></span><div><p class="t">Staff Area</p><p class="tx">Changing rooms and staff lunch room.</p></div></div>
      <div class="row"><span class="ic sm grey"><svg><use href="#i-screen"/></svg></span><div><p class="t">Storage</p><p class="tx">Racking for goods and materials.</p></div></div>
      <div class="row"><span class="ic sm grey"><svg><use href="#i-screen"/></svg></span><div><p class="t grey">Loading Zone</p><p class="tx">Docks facing the harbour road.</p></div></div>
    </div>
    <div class="ph ph-interior" role="img" aria-label="Photo of the lower floor workshop hall"></div>
    <div class="tile-quote"><svg viewBox="0 0 16 16"><use href="#i-quote"/></svg></div>
    <div class="tile-gold"><p class="tx">Add a short note here about the lower floor to support the picture beside it on the slide.</p></div>
    <p class="url">www.brevikhamna.se</p><span class="pg"></span>
  </section>

  <!-- 28 get in touch -->
  <section class="slide contact">
    <div class="ph ph-building" role="img" aria-label="Photo of the company building with its front car park"></div>
    <p class="addr">Hamngatan 4<br>452 30 Strömstad<br>Sverige</p>
    <div class="contact-bar">
      <h3>Get In Touch</h3>
      <div class="row"><span class="ic"><svg><use href="#i-mail"/></svg></span><div><b>kontakt@brevikhamna.se</b><span>We are here to help you</span></div></div>
      <div class="row"><span class="ic gold"><svg><use href="#i-phone"/></svg></span><div><b class="gold">01 2020 3030</b><span>Working days 8am to 7pm</span></div></div>
    </div>
  </section>

</main>
</body>
</html>
```